NEW FACEBOOK AD CREATIVES FOR MARKETING AGENCY

We need one single static image AND a Carousel Ad Design With 5 Cards Total in it.

We advertise a SaaS Product that teaches businesses how to use incentive based marketing to get more sales and leads.

Using our service businesses can give away smart devices like smartwatches, earpods, mp4 players, tablets, etc. as a gift bonus along with their product or service as an added value benefit to help them create more attractive offers and to get more sales.

I have attached two designs that get me my best results on facebook ads so far so I want to create something very similar with a different look and showcasing 3-4 of the items I have attached images for.

CONTENT & INSTRUCTIONS:
MAIN TEXT: TRIPLE YOUR SALES OFFERING FREE SMART DEVICES AS A BONUS FOR BUYING YOUR PRODUCT OR SERVICE

Target Market(s)

ENTREPRENEURS, INVESTORS, BUSINESS OWNERS, MEDIA AGENCIES, BROKERAGES

Industry/Entity Type

marketing gifting

Requirements
Must have
• must match color scheme of website www.brightlanepromoworks.biz as this is where they will be redirected to when they click.
Nice to have
• the ads must be 1080x1080 Static newsfeed ad and carousel ads

```html
<!DOCTYPE html>
<html lang="en">
<head>
<meta charset="utf-8">
<title>Brightlane Promo Works – Ad Design and Carousel Ad</title>
<link href="https://fonts.googleapis.com/css2?family=Poppins:wght@400;500;600;700;800&display=swap" rel="stylesheet">
<style>
  :root{
    --board-top:#d5d8e3;
    --board-bottom:#97a0dc;
    --label:#24226d;
    --navy:#241c6e;
    --navy-soft:#3a2f92;
    --white:#ffffff;
    --corner-grey:#b9bbc6;
    --green:#3ff23a;
    --teal:#1fc7c9;
    --sky:#22b4f0;
    --blue:#1a7fd4;
    --orange:#ff3d00;
    --pill:#2746b0;
    --brand-blue:#4aa3ff;
    --brand-navy:#26338a;
  }
  *{box-sizing:border-box;margin:0;padding:0}
  html,body{width:908px;height:1200px;overflow:hidden}
  body{position:relative;font-family:"Poppins",sans-serif;background:var(--board-bottom)}

  .board-top{position:absolute;left:0;top:0;width:908px;height:600px;background:var(--board-top)}
  .board-bottom{position:absolute;left:0;top:600px;width:908px;height:600px;background:var(--board-bottom)}

  .section-label{position:absolute;color:var(--label);writing-mode:vertical-rl;transform:rotate(180deg);white-space:nowrap;line-height:1}
  .section-label--ad{left:108px;top:163px;font-size:38px;font-weight:500;letter-spacing:1px}
  .section-label--carousel{left:770px;top:930px;font-size:42px;font-weight:400}

  /* ---------- static ad ---------- */
  .static-ad{position:absolute;left:204px;top:48px;width:500px;height:500px;overflow:hidden;box-shadow:0 3px 10px rgba(20,20,60,.25)}
  .static-ad svg.static-ad__bg{position:absolute;left:0;top:0}
  .brand{position:absolute;display:flex;align-items:center;gap:8px;font-weight:700;line-height:1.05;text-transform:uppercase;white-space:nowrap}
  .brand__dot{border-radius:50%;flex:none}
  .static-ad .brand{left:32px;top:44px;color:var(--brand-navy);font-size:22px}
  .static-ad .brand__dot{width:22px;height:22px;background:var(--brand-navy)}

  .headline{position:absolute;color:var(--green);font-weight:800;text-align:center;text-transform:uppercase;line-height:.8;letter-spacing:-1px;white-space:nowrap}
  .static-ad .headline{left:262px;top:116px;width:226px;font-size:66px}

  .cta{position:absolute;color:var(--white);font-weight:600;text-align:center;text-transform:uppercase;line-height:1.2;white-space:nowrap}
  .static-ad .cta{left:126px;top:411px;width:140px;height:39px;border-radius:20px;background:var(--orange);font-size:10.5px;padding-top:6px}

  .offer{position:absolute;color:var(--white);font-weight:700;text-transform:uppercase;line-height:1.28;white-space:nowrap}
  .offer__accent{color:var(--orange)}
  .static-ad .offer{left:286px;top:400px;font-size:13px}

  .product{position:absolute;border-radius:14px}
  .product--watch{background:radial-gradient(circle at 45% 45%,#3d3d46,#111117 70%)}
  .product--earbuds{background:linear-gradient(150deg,#ffffff,#cfd2d8)}
  .product--headphones{background:radial-gradient(circle at 40% 40%,#4a4a52,#0f0f14 70%)}
  .product--speaker{background:linear-gradient(150deg,#b5b7bd,#55575e)}
  .product--phone{background:linear-gradient(160deg,#2c63d6,#0f1230)}
  .product--player{background:linear-gradient(150deg,#3a3a44,#050508)}
  .product--laptop{background:linear-gradient(160deg,#6b3fb0,#2a2a35 70%,#a9a9ad)}
  .product--tablet{background:linear-gradient(150deg,#3a84d6,#1d2b55 80%)}
  .product--purple-headphones{background:radial-gradient(circle at 40% 40%,#c23ad6,#4a1c8a 70%)}
  .product--bluetooth-speaker{background:linear-gradient(150deg,#4a5566,#1b2230)}

  /* ---------- carousel cards ---------- */
  .card{position:absolute;width:280px;height:280px;overflow:hidden;box-shadow:0 2px 8px rgba(20,20,60,.25)}
  .card svg.card__bg{position:absolute;left:0;top:0}
  .card .brand{top:20px;width:140px;justify-content:center;color:var(--brand-blue);font-size:12px;gap:5px}
  .card .brand__dot{width:11px;height:11px;background:var(--brand-blue)}
  .card .headline{top:80px;width:140px;font-size:37px}
  .card .cta{left:101px;top:194px;width:79px;height:22px;border-radius:11px;background:var(--pill);border:1.5px solid #4f7be6;font-size:6.6px;padding-top:3px;line-height:1.15}
  .card .offer{left:87px;top:229px;font-size:7.6px;line-height:1.24}
  .card--text-left .brand,.card--text-left .headline{left:6px}
  .card--text-right .brand,.card--text-right .headline{left:138px}
  .card .product{border-radius:10px}
</style>
</head>
<body>

<div class="board-top"></div>
<div class="board-bottom"></div>

<div class="section-label section-label--ad">AD DESIGN</div>
<div class="section-label section-label--carousel">Carousel Ad</div>

<!-- ===== Static newsfeed ad ===== -->
<section class="static-ad">
  <svg class="static-ad__bg" width="500" height="500" viewBox="0 0 500 500">
    <defs>
      <clipPath id="navy-field">
        <path d="M0 166 L244 110 L244 212 L0 212 Z"/>
        <circle cx="380" cy="212" r="170"/>
        <rect x="0" y="200" width="500" height="300"/>
      </clipPath>
      <radialGradient id="team-tint" cx="0.6" cy="0.55" r="0.6">
        <stop offset="0" stop-color="#4a4fb8" stop-opacity=".55"/>
        <stop offset="1" stop-color="#241c6e" stop-opacity="0"/>
      </radialGradient>
      <radialGradient id="dial-glow" cx="0.5" cy="0.5" r="0.5">
        <stop offset="0" stop-color="#241c6e" stop-opacity="0"/>
        <stop offset=".7" stop-color="#2ad89a" stop-opacity=".18"/>
        <stop offset=".9" stop-color="#22b4f0" stop-opacity=".28"/>
        <stop offset="1" stop-color="#241c6e" stop-opacity="0"/>
      </radialGradient>
      <linearGradient id="frame-glow" x1="0" y1="0" x2="1" y2="1">
        <stop offset="0" stop-color="#3ff23a" stop-opacity=".22"/>
        <stop offset="1" stop-color="#1fc7c9" stop-opacity=".12"/>
      </linearGradient>
    </defs>
    <rect width="500" height="500" fill="var(--white)"/>
    <polygon points="362,0 500,0 500,97" fill="var(--corner-grey)"/>
    <g clip-path="url(#navy-field)">
      <rect width="500" height="500" fill="var(--navy)"/>
      <rect width="500" height="500" fill="url(#team-tint)" role="img" aria-label="Photo of a smiling business team at work, tinted navy"/>
    </g>
    <circle cx="347" cy="212" r="150" fill="url(#dial-glow)" role="img" aria-label="Circular progress dial decoration in green and blue"/>
    <rect x="28" y="192" width="156" height="168" rx="20" fill="url(#frame-glow)" role="img" aria-label="Triangular glowing frame decoration around the products"/>
    <polygon points="0,436 0,500 62,500" fill="var(--blue)"/>
    <circle cx="93" cy="454" r="18" fill="var(--green)"/>
  </svg>

  <div class="brand"><span class="brand__dot"></span><span>Brightlane<br>Promo Works</span></div>
  <div class="headline">3X<br>Your<br>Sales</div>

  <div class="product product--watch" style="left:64px;top:209px;width:104px;height:124px;border-radius:50px" role="img" aria-label="Black smartwatch showing the time 09:35"></div>
  <div class="product product--earbuds" style="left:29px;top:337px;width:106px;height:121px" role="img" aria-label="White wireless earbuds in an open charging case"></div>

  <div class="cta">Get a free<br>sample package</div>
  <p class="offer"><span class="offer__accent">Offering free smart<br>devices</span> as a bonus for<br>buying your product<br>or service</p>
</section>

<!-- ===== Carousel card 1 ===== -->
<section class="card card--text-left" style="left:25px;top:614px">
  <svg class="card__bg" width="280" height="280" viewBox="0 0 280 280">
    <defs>
      <linearGradient id="tile" x1="0" y1="0" x2="0" y2="1">
        <stop offset="0" stop-color="#3ff23a"/>
        <stop offset=".5" stop-color="#1fc7c9"/>
        <stop offset="1" stop-color="#22b4f0"/>
      </linearGradient>
      <radialGradient id="crowd" cx="0.3" cy="0.4" r="0.7">
        <stop offset="0" stop-color="#4a4fb8" stop-opacity=".5"/>
        <stop offset="1" stop-color="#241c6e" stop-opacity="0"/>
      </radialGradient>
    </defs>
    <rect width="280" height="280" fill="var(--navy)"/>
    <rect width="280" height="204" fill="url(#crowd)" role="img" aria-label="Photo of a cheerful team, tinted navy"/>
    <polygon points="135,0 245,0 190,45" fill="var(--corner-grey)"/>
    <rect y="204" width="280" height="76" fill="var(--orange)"/>
    <rect x="175" y="69" width="170" height="170" rx="26" transform="rotate(45 260 154)" fill="var(--navy-soft)" opacity=".8"/>
    <rect x="179" y="73" width="162" height="162" rx="22" transform="rotate(45 260 154)" fill="url(#tile)"/>
    <circle cx="157" cy="88" r="7" fill="var(--green)"/>
    <circle cx="52" cy="198" r="22" fill="var(--green)"/>
  </svg>
  <div class="brand"><span class="brand__dot"></span><span>Brightlane<br>Promo Works</span></div>
  <div class="headline">3X<br>Your<br>Sales</div>
  <div class="product product--watch" style="left:156px;top:8px;width:64px;height:74px" role="img" aria-label="Square smartwatch with app icons"></div>
  <div class="product product--headphones" style="left:236px;top:67px;width:44px;height:118px" role="img" aria-label="Black and gold over-ear headphones"></div>
  <div class="product product--earbuds" style="left:18px;top:176px;width:54px;height:69px" role="img" aria-label="White wireless earbuds"></div>
  <div class="cta">Get a free<br>sample package</div>
  <p class="offer">Offering free smart<br>devices as a bonus for<br>buying your product<br>or service</p>
</section>

<!-- ===== Carousel card 2 ===== -->
<section class="card card--text-right" style="left:314px;top:614px">
  <svg class="card__bg" width="280" height="280" viewBox="0 0 280 280">
    <rect width="280" height="280" fill="var(--navy)"/>
    <rect width="280" height="204" fill="url(#crowd)" role="img" aria-label="Photo of a cheerful team, tinted navy"/>
    <rect y="204" width="280" height="76" fill="var(--orange)"/>
    <rect x="-35" y="51" width="170" height="170" rx="26" transform="rotate(45 50 136)" fill="var(--navy-soft)" opacity=".8"/>
    <rect x="-31" y="55" width="162" height="162" rx="22" transform="rotate(45 50 136)" fill="url(#tile)"/>
    <circle cx="230" cy="192" r="22" fill="var(--green)"/>
  </svg>
  <div class="brand"><span class="brand__dot"></span><span>Brightlane<br>Promo Works</span></div>
  <div class="headline">3X<br>Your<br>Sales</div>
  <div class="product product--headphones" style="left:25px;top:12px;width:94px;height:82px" role="img" aria-label="Folded black wireless headphones"></div>
  <div class="product product--headphones" style="left:0;top:64px;width:56px;height:121px" role="img" aria-label="Black over-ear headphones seen from the side"></div>
  <div class="product product--speaker" style="left:200px;top:194px;width:67px;height:66px" role="img" aria-label="Grey cube speaker"></div>
  <div class="cta">Get a free<br>sample package</div>
  <p class="offer">Offering free smart<br>devices as a bonus for<br>buying your product<br>or service</p>
</section>

<!-- ===== Carousel card 3 ===== -->
<section class="card card--text-left" style="left:603px;top:614px">
  <svg class="card__bg" width="280" height="280" viewBox="0 0 280 280">
    <rect width="280" height="280" fill="var(--navy)"/>
    <rect width="280" height="204" fill="url(#crowd)" role="img" aria-label="Photo of a cheerful team, tinted navy"/>
    <polygon points="135,0 245,0 190,45" fill="var(--corner-grey)"/>
    <rect y="204" width="280" height="76" fill="var(--orange)"/>
    <rect x="175" y="69" width="170" height="170" rx="26" transform="rotate(45 260 154)" fill="var(--navy-soft)" opacity=".8"/>
    <rect x="179" y="73" width="162" height="162" rx="22" transform="rotate(45 260 154)" fill="url(#tile)"/>
    <circle cx="155" cy="80" r="7" fill="var(--green)"/>
  </svg>
  <div class="brand"><span class="brand__dot"></span><span>Brightlane<br>Promo Works</span></div>
  <div class="headline">3X<br>Your<br>Sales</div>
  <div class="product product--phone" style="left:175px;top:12px;width:33px;height:76px;border-radius:6px" role="img" aria-label="Smartphone showing its home screen"></div>
  <div class="product product--watch" style="left:196px;top:97px;width:78px;height:88px" role="img" aria-label="Black smartwatch showing the time"></div>
  <div class="product product--player" style="left:12px;top:173px;width:81px;height:97px" role="img" aria-label="Black portable media player"></div>
  <div class="cta">Get a free<br>sample package</div>
  <p class="offer">Offering free smart<br>devices as a bonus for<br>buying your product<br>or service</p>
</section>

<!-- ===== Carousel card 4 ===== -->
<section class="card card--text-right" style="left:167px;top:906px">
  <svg class="card__bg" width="280" height="280" viewBox="0 0 280 280">
    <rect width="280" height="280" fill="var(--navy)"/>
    <rect width="280" height="204" fill="url(#crowd)" role="img" aria-label="Photo of a cheerful team, tinted navy"/>
    <rect y="204" width="280" height="76" fill="var(--orange)"/>
    <rect x="-37" y="50" width="170" height="170" rx="26" transform="rotate(45 48 135)" fill="var(--navy-soft)" opacity=".8"/>
    <rect x="-33" y="54" width="162" height="162" rx="22" transform="rotate(45 48 135)" fill="url(#tile)"/>
    <circle cx="100" cy="28" r="8" fill="var(--green)"/>
    <circle cx="228" cy="196" r="20" fill="var(--green)"/>
  </svg>
  <div class="brand"><span class="brand__dot"></span><span>Brightlane<br>Promo Works</span></div>
  <div class="headline">3X<br>Your<br>Sales</div>
  <div class="product product--laptop" style="left:5px;top:24px;width:154px;height:94px" role="img" aria-label="Open laptop showing a tiled start screen"></div>
  <div class="product product--earbuds" style="left:2px;top:120px;width:79px;height:75px" role="img" aria-label="White earbuds charging case"></div>
  <div class="product product--earbuds" style="left:205px;top:178px;width:57px;height:48px" role="img" aria-label="Pair of white wireless earbuds"></div>
  <div class="cta">Get a free<br>sample package</div>
  <p class="offer">Offering free smart<br>devices as a bonus for<br>buying your product<br>or service</p>
</section>

<!-- ===== Carousel card 5 ===== -->
<section class="card card--text-left" style="left:457px;top:906px">
  <svg class="card__bg" width="280" height="280" viewBox="0 0 280 280">
    <rect width="280" height="280" fill="var(--navy)"/>
    <rect width="280" height="204" fill="url(#crowd)" role="img" aria-label="Photo of a cheerful team, tinted navy"/>
    <polygon points="132,0 240,0 186,40" fill="var(--corner-grey)"/>
    <rect y="204" width="280" height="76" fill="var(--orange)"/>
    <rect x="175" y="45" width="170" height="170" rx="26" transform="rotate(45 260 130)" fill="var(--navy-soft)" opacity=".8"/>
    <rect x="179" y="49" width="162" height="162" rx="22" transform="rotate(45 260 130)" fill="url(#tile)"/>
    <circle cx="200" cy="65" r="8" fill="var(--green)"/>
    <circle cx="55" cy="200" r="20" fill="var(--green)"/>
  </svg>
  <div class="brand"><span class="brand__dot"></span><span>Brightlane<br>Promo Works</span></div>
  <div class="headline">3X<br>Your<br>Sales</div>
  <div class="product product--bluetooth-speaker" style="left:178px;top:7px;width:80px;height:38px;border-radius:18px" role="img" aria-label="Cylindrical portable speaker"></div>
  <div class="product product--tablet" style="left:154px;top:81px;width:115px;height:115px" role="img" aria-label="Tablet in a stand case showing app icons"></div>
  <div class="product product--purple-headphones" style="left:9px;top:196px;width:67px;height:70px" role="img" aria-label="Purple wireless headphones"></div>
  <div class="cta">Get a free<br>sample package</div>
  <p class="offer">Offering free smart<br>devices as a bonus for<br>buying your product<br>or service</p>
</section>

</body>
</html>
```